Menu for burgers the restaurant will be called 'THE LANTERN'

something special that reflects the image of a relaxed and friendly bar.
you will find a picture of a menu for inspiration.
Some examples uploaded

Target Market(s)

all categories who search for simple and funny bar for watching football

Requirements
Must have
• some funny emoticons
font style - like the picture of the menu uploaded
if you can do the same menu it will be perfect !!! the cow at the background etc...
Nice to have
• black font style and colorful wall (not too much) simple and elegant
Should not have
• a lot of colours
serious emoticons

```html
<!DOCTYPE html>
<html lang="fr">
<head>
<meta charset="utf-8">
<title>The Lantern – Burger Menu</title>
<link href="https://fonts.googleapis.com/css2?family=Oswald:wght@400;500;600&family=Fira+Sans+Condensed:wght@400;500&display=swap" rel="stylesheet">
<style>
  :root{
    --paper:#ecdfcb;
    --brown:#4f2218;
    --ink:#4a2a20;
    --orange:#d9731c;
    --cream:#f3e6d2;
    --yellow:#f3c64a;
  }
  *{box-sizing:border-box;margin:0;padding:0}
  html,body{width:1200px;height:800px;overflow:hidden;background:var(--paper)}
  .menu{position:relative;width:1200px;height:800px;overflow:hidden;background:var(--paper);
    font-family:"Fira Sans Condensed",sans-serif;color:var(--ink)}
  .rule{position:absolute;background:var(--brown)}
  .rule.thin{height:2px}
  .rule.thick{height:5px}
  .rule.orange{background:var(--orange)}

  .side-label{position:absolute;writing-mode:vertical-rl;transform:rotate(180deg);
    font-family:"Oswald",sans-serif;font-weight:500;font-size:19px;letter-spacing:.5px;
    color:var(--cream);text-align:center;line-height:30px;white-space:nowrap}
  .side-label.brown{background:var(--brown)}
  .side-label.orange{background:var(--orange)}
  .side-label.small{font-size:17px;letter-spacing:0}

  .item{position:absolute}
  .item-head{display:flex;align-items:baseline}
  .item-name{font-family:"Oswald",sans-serif;font-weight:500;font-size:16px;color:var(--brown);text-transform:uppercase;line-height:20px}
  .item-price{margin-left:auto;font-family:"Oswald",sans-serif;font-size:12px;color:var(--orange);white-space:nowrap}
  .item-desc{font-size:12px;line-height:14px;color:var(--ink)}
  .item-sub{font-family:"Oswald",sans-serif;font-size:11px;color:var(--brown);line-height:14px}

  .illustration{position:absolute}
  .brand-ring{position:absolute;left:425px;top:125px;width:350px;height:350px;border-radius:50%;border:4px solid var(--orange)}
  .brand-disc{position:absolute;left:443px;top:143px;width:314px;height:314px;border-radius:50%;
    background:radial-gradient(circle at 50% 50%,#d9802c 0%,#c9651a 70%,#b85814 100%)}
  .brand-name{position:absolute;left:443px;top:225px;width:314px;text-align:center;
    font-family:"Oswald",sans-serif;font-weight:600;font-size:58px;line-height:64px;color:var(--yellow);letter-spacing:1px}
  .brand-sub{position:absolute;left:443px;top:358px;width:314px;text-align:center;
    font-family:"Oswald",sans-serif;font-weight:600;font-size:13px;color:var(--yellow);letter-spacing:.5px}
  .top-tab{position:absolute;left:533px;top:0;width:132px;height:50px;background:var(--orange)}

  .extras{position:absolute;left:808px;top:307px;width:345px;font-size:11px;line-height:14px;color:var(--ink)}
  .extras b{font-family:"Oswald",sans-serif;font-weight:500;color:var(--brown)}
  .dash{position:absolute;left:808px;top:391px;width:345px;border-top:2px dashed var(--brown)}

  .banner{position:absolute;font-family:"Oswald",sans-serif;color:var(--cream);display:flex;align-items:center}
  .banner.salades{left:806px;top:393px;width:168px;height:34px;background:var(--brown);font-size:22px;padding-left:34px}
  .banner.kids{left:490px;top:546px;width:470px;height:48px;background:var(--orange);font-size:15px;justify-content:center;letter-spacing:.3px}

  .ask-badge{position:absolute;left:88px;top:598px;width:98px;height:56px;border-radius:50%;background:var(--orange);
    font-family:"Oswald",sans-serif;font-size:12px;line-height:14px;color:var(--brown);text-align:center;padding-top:13px}
  .ask-badge span{color:var(--yellow);font-size:13px}

  .list{position:absolute;font-family:"Oswald",sans-serif;color:var(--brown)}
  .list .row{display:flex;align-items:baseline;font-size:16px;line-height:21.5px;white-space:nowrap}
  .list .row .p{margin-left:auto;font-size:12px;color:var(--orange)}
  .list.kids .row{position:relative;line-height:23px}
  .list.kids .row .p{margin-left:0;position:absolute;left:120px}
  .list.student .row{line-height:22px}

  .student-box{position:absolute;left:985px;top:540px;width:165px;height:116px;background:var(--brown);
    font-family:"Oswald",sans-serif;color:var(--cream);font-size:14px;line-height:17px;padding:8px 10px}
  .student-box .note{color:var(--yellow);font-size:13px;line-height:16px;display:block}
</style>
</head>
<body>
<main class="menu">

  <!-- Beef burgers -->
  <div class="rule thick" style="left:45px;top:29px;width:295px"></div>
  <div class="rule thin" style="left:45px;top:38px;width:295px"></div>
  <div class="side-label brown" style="left:48px;top:55px;width:30px;height:130px">BŒUF</div>
  <div class="side-label orange" style="left:48px;top:185px;width:30px;height:135px">BURGERS</div>

  <section class="beef">
    <div class="item" style="left:90px;top:52px;width:250px"><div class="item-head"><span class="item-name">Big Beef</span><span class="item-price">8.9.-/13.9.-</span></div><p class="item-desc">Ketchup, cornichons, oignons caramélisés, tomate, salade, sauce maison</p></div>
    <div class="item" style="left:90px;top:116px;width:250px"><div class="item-head"><span class="item-name">Big Cheese</span><span class="item-price">10.9.-/15.9.-</span></div><p class="item-desc">Cheddar, ketchup, cornichons, oignons caramélisés, salade, sauce maison</p></div>
    <div class="item" style="left:90px;top:172px;width:250px"><div class="item-head"><span class="item-name">Mexicana Beef</span><span class="item-price">12.9.-/17.9.-</span></div><p class="item-desc">Guacamole, ketchup, oignons caramélisés, salade, sauce piquante maison</p></div>
    <div class="item" style="left:90px;top:228px;width:250px"><div class="item-head"><span class="item-name">The Special One</span><span class="item-price">12.9.-/17.9.-</span></div><p class="item-desc">Purée de tomate maison, œuf, huile d'olive, persil, sauce maison</p></div>
    <div class="item" style="left:90px;top:284px;width:250px"><div class="item-head"><span class="item-name">Red Hot Chili Burger</span><span class="item-price">12.9.-/17.9.-</span></div><p class="item-desc">Cheddar, oignons caramélisés, Tomate, Salade, sauce piquante maison</p></div>
    <div class="item" style="left:90px;top:340px;width:250px"><div class="item-head"><span class="item-name">Die Schweizer</span><span class="item-price">12.9.-/17.9.-</span></div><p class="item-desc">Fromage à raclette aux poivres, cornichon, salade, oignons caramélisés, sauce moutarde</p></div>
    <div class="item" style="left:90px;top:395px;width:250px"><div class="item-head"><span class="item-name">The Goat</span><span class="item-price">13.9.-/18.9.-</span></div><p class="item-desc">Bacon, rondelle de chèvre, miel, oignons caramélisés, salade, sauce maison</p></div>
    <div class="item" style="left:90px;top:451px;width:250px"><div class="item-head"><span class="item-name">El Matador</span><span class="item-price">12.9.-/17.9.-</span></div><p class="item-desc">Chorizo, jalapenos, tomate, salade, sauce aioli maison</p></div>
    <div class="item" style="left:90px;top:507px;width:250px"><div class="item-head"><span class="item-name">Smokey Beef</span><span class="item-price">12.9.-/17.9.-</span></div><p class="item-desc">Bacon, cheddar, oignons caramélisés, onion rings, salade, sauce BBQ</p></div>
  </section>

  <!-- Competition burgers -->
  <div class="rule thick" style="left:45px;top:557px;width:440px"></div>
  <div class="rule thin" style="left:45px;top:566px;width:440px"></div>
  <div class="side-label brown" style="left:47px;top:570px;width:32px;height:86px">BURGERS</div>
  <div class="side-label orange small" style="left:47px;top:656px;width:32px;height:124px">COMPETITION</div>
  <div class="ask-badge">DEMANDEZ LES<br><span>AVANT 20MIN'</span></div>

  <section class="competition">
    <div class="item" style="left:192px;top:566px;width:255px"><div class="item-head"><span class="item-name">The Monster 'Big Mouth Burger' -</span></div><p class="item-sub">SI FINI EN 15 MIN &nbsp;|&nbsp; DESSERT OFFERT <span class="item-price" style="margin-left:40px">39.9.-</span></p><p class="item-desc" style="margin-top:4px">Triple Beef, triple cheddar, cornichons, salade, tomate, sauce maison.<br>Double ration de frites et boisson</p></div>
    <div class="item" style="left:192px;top:654px;width:265px"><div class="item-head"><span class="item-name">Rolling Hill Burger -</span></div><p class="item-sub">SI FINI EN 10 MIN &nbsp;|&nbsp; CHICHA OFFERTE <span class="item-price" style="margin-left:40px">69.9.-</span></p><p class="item-desc" style="margin-top:4px">Quintuple Beef, quintuple cheddar, cornichons, onion rings, salade, tomate, sauce maison.<br>Frites cheddar et boisson</p></div>
  </section>
  <div class="rule thin orange" style="left:85px;top:765px;width:400px"></div>
  <div class="rule thick" style="left:85px;top:770px;width:400px"></div>

  <!-- Illustration areas -->
  <div class="illustration" role="img" aria-label="Sketch of a burger" style="left:360px;top:30px;width:135px;height:100px;border-radius:50% 50% 40% 40%;background:radial-gradient(ellipse at 50% 45%,#c9a98a 0%,#b58c6a 60%,rgba(181,140,106,0) 72%)"></div>
  <div class="illustration" role="img" aria-label="Sketch of a burger with a sauce bottle and fries" style="left:345px;top:400px;width:140px;height:150px;background:radial-gradient(ellipse at 45% 50%,#c9a98a 0%,#d9a860 45%,rgba(217,168,96,0) 70%)"></div>
  <div class="illustration" role="img" aria-label="Sketch of a salad bowl" style="left:660px;top:425px;width:140px;height:90px;border-radius:0 0 50% 50%;background:radial-gradient(ellipse at 50% 40%,#b99a7c 0%,#a88466 55%,rgba(168,132,102,0) 72%)"></div>
  <div class="illustration" role="img" aria-label="Sketch of a soft drink cup and fries" style="left:515px;top:702px;width:170px;height:60px;background:radial-gradient(ellipse at 50% 50%,#b99a7c 0%,#a88466 50%,rgba(168,132,102,0) 72%)"></div>

  <!-- Centre brand -->
  <div class="top-tab"></div>
  <div class="brand-ring"></div>
  <div class="brand-disc" role="img" aria-label="Sketched burger illustration behind the name"></div>
  <div class="brand-name">THE<br>LANTERN</div>
  <div class="brand-sub">BURGER MENU</div>

  <!-- Chicken burgers -->
  <div class="rule thick" style="left:858px;top:20px;width:292px"></div>
  <div class="rule thin" style="left:858px;top:30px;width:292px"></div>
  <div class="side-label orange" style="left:808px;top:25px;width:30px;height:110px">POULET</div>
  <div class="side-label brown" style="left:808px;top:135px;width:30px;height:115px">BURGERS</div>

  <section class="chicken">
    <div class="item" style="left:858px;top:53px;width:292px"><div class="item-head"><span class="item-name">The Crispy</span><span class="item-price">12.9.-/17.9.-</span></div><p class="item-desc">Poulet panné, cheddar, oignons caramélisés, salade, sauce tartare</p></div>
    <div class="item" style="left:858px;top:109px;width:292px"><div class="item-head"><span class="item-name">Mexicana Chiken</span><span class="item-price">12.9.-/17.9.-</span></div><p class="item-desc">Poulet panné, Guacamole, oignons caramélisés, salade, sauce piquante, Sauce maison Lime et Basilic</p></div>
    <div class="item" style="left:858px;top:162px;width:292px"><div class="item-head"><span class="item-name">Grecos</span><span class="item-price">13.9.-/18.9.-</span></div><p class="item-desc">Tomate, salade, feta, aubergine grillée, tzaziki, Sauce maison Lime et Basilic</p></div>
    <div class="item" style="left:858px;top:217px;width:292px"><div class="item-head"><span class="item-name">Burger Veggie</span><span class="item-price">12.9.-/17.9.-</span></div><p class="item-desc">Tomate, salade, oignons caramélisés, sauce maison Lime et Basilic</p></div>
  </section>

  <p class="extras"><b>SUPPLÉMENTS VIANDES :</b> Bœuf (160g) 4.5 Poulet (120g) 4.-<br><b>TOPPINGS :</b> Fromage, œuf, bacon, chorizo, guacamole, oignons caramélisés. 2.-<br><b>UPGRADE :</b> Patates douces / Potatoes 2.- , Milkshake classique +3.- , Bière +3.-. &nbsp;&nbsp;<b>Viande Halal sur demande</b></p>
  <div class="dash"></div>

  <div class="banner salades">SALADES</div>
  <section class="salads">
    <div class="item" style="left:808px;top:430px;width:345px"><div class="item-head"><span class="item-name">Chiken Salad</span><span class="item-price">16.9.-</span></div><p class="item-desc" style="width:330px">Filet de poulet, salade, Tomate, gruyère AOP, onion rings, sauce au citron vert</p></div>
    <div class="item" style="left:808px;top:486px;width:345px"><div class="item-head"><span class="item-name">Hawai</span><span class="item-price">17.9.-</span></div><p class="item-desc" style="width:330px">Crevettes roses, ananas, avocats, concombre, coriandre, feuilles de salade, sauce cocktails</p></div>
  </section>

  <!-- Kids menu and sides -->
  <div class="banner kids">MENU ENFANT (AVEC BOISSON SANS ALCOOL ET FRITES)</div>
  <div class="list kids" style="left:493px;top:603px;width:200px">
    <div class="row">JUNIOR BEEF<span class="p">6,9.- / 10,9.-</span></div>
    <div class="row">JUNIOR CHEESE<span class="p">7,9.- / 11,9.-</span></div>
    <div class="row">JUNIOR CRISPY<span class="p">7,9.- / 11,9.-</span></div>
    <div class="row">JUNIOR VEGGIE<span class="p">7,9.- / 11,9.-</span></div>
  </div>
  <div class="list sides" style="left:700px;top:603px;width:260px">
    <div class="row">ONION RINGS &nbsp;(4 PIÈCES)<span class="p">4,9.-</span></div>
    <div class="row">FRITES<span class="p">4,9.-</span></div>
    <div class="row">PATATES DOUCES<span class="p">5,9.-</span></div>
    <div class="row">POTATOES<span class="p">5,9.-</span></div>
    <div class="row">PATATAS BRAVAS<span class="p">8,9.-</span></div>
    <div class="row">FILETS DE POULETS 'TENDERS'<span class="p">12,9.-</span></div>
    <div class="row">BEEF CHILI CHEESE FRIES<span class="p">14,9.-</span></div>
  </div>
  <div class="rule thick" style="left:485px;top:765px;width:475px"></div>
  <div class="rule thin orange" style="left:485px;top:773px;width:475px"></div>

  <!-- Student menu -->
  <div class="student-box">MENU ETUDIANT &nbsp;(AVEC BOISSON SANS ALCOOL ET FRITES):<span class="note">UN MENU PAR CARTE D'ÉTUDIANT</span></div>
  <div class="list student" style="left:1005px;top:668px;width:145px">
    <div class="row">BIG BEEF<span class="p">11,9.-</span></div>
    <div class="row">BIG CHEESE<span class="p">12,9.-</span></div>
    <div class="row">THE CRISPY<span class="p">12,9.-</span></div>
    <div class="row">THE VEGGIE<span class="p">12,9.-</span></div>
  </div>
  <div class="rule thick" style="left:985px;top:765px;width:165px"></div>
  <div class="rule thin orange" style="left:985px;top:773px;width:165px"></div>

</main>
</body>
</html>
```